LED Bannerwerbung im Fußballstadion des SV Blitzhafen Murnau!
Zielgruppe
Die welmora hotels & resorts GmbH ist ein mittelständisches Familienunternehmen mit aktuell 25 Hotelbetreiben und ist Sponsor des SV Blitzhafen Murnau.
Aufgabenstellung
Wir haben eine LED Bandenwerbung in den Massen 4608px x 80px und möchten diese erneuern.
Längere Standzeit Logo - Animation ja aber nicht so lange. Witzig und spritzig . Im Kern sind wir
Spezialisten für Kurztrips im Osten.

```html
<!DOCTYPE html>
<html lang="de">
<head>
<meta charset="utf-8">
<title>welmora hotels – LED Bandenwerbung</title>
<link href="https://fonts.googleapis.com/css2?family=Montserrat:wght@300;700&display=swap" rel="stylesheet">
<style>
  :root {
    --stage: #000000;
    --band: #ffffff;
    --orange: #ee7d22;
    --blue: #2a9ad8;
    --road-teal: #1aa9a0;
    --road-green: #8fcdb0;
    --road-light: #c7dbe2;
    --map: #f5b331;
    --sign: #d98a3a;
    --compass: #2fb0a0;
    --plane: #2fb0a0;
    --passport: #f5b331;
    --camera: #e8553f;
    --suitcase: #f0a030;
    --label: #ffffff;
  }
  html, body { margin: 0; padding: 0; overflow: hidden; }
  body { width: 1200px; height: 2804px; background: var(--stage); position: relative; font-family: "Montserrat", sans-serif; }

  .band { position: absolute; top: 69px; height: 2667px; width: 46px; background: var(--band); overflow: hidden; }
  .band--text { left: 261px; }
  .band--plain { left: 824px; }

  .item { position: absolute; left: 0; width: 100%; display: flex; align-items: center; justify-content: center; }
  .vertical { writing-mode: vertical-rl; transform: rotate(180deg); white-space: nowrap; }

  /* winding road segments hugging the band edges */
  .road { width: 32px; }
  .road--left { left: 0; border-radius: 0 20px 20px 0; }
  .road--right { left: auto; right: 0; border-radius: 20px 0 0 20px; }
  .road--light { background: linear-gradient(180deg, var(--road-light), #dde9ed); }
  .road--green { background: linear-gradient(180deg, var(--road-green), var(--road-teal)); }
  .road--teal { background: linear-gradient(180deg, var(--road-teal), #1f8fc0); }

  /* travel pictograms, each a single flat tone */
  .icon { width: 34px; left: 6px; border-radius: 6px; }
  .icon--map { background: var(--map); transform: rotate(-12deg); }
  .icon--sign { background: var(--sign); width: 30px; left: 8px; border-radius: 3px; }
  .icon--compass { background: none; border: 4px solid var(--compass); border-radius: 50%; width: 22px; left: 8px; box-sizing: content-box; }
  .icon--plane { background: var(--plane); border-radius: 50% 50% 40% 40%; transform: rotate(20deg); }
  .icon--passport { background: var(--passport); transform: rotate(-10deg); border-radius: 4px; }
  .icon--camera { background: var(--camera); transform: rotate(-15deg); border-radius: 8px; }
  .icon--suitcase { background: var(--suitcase); border-radius: 4px; }

  .slogan { font-weight: 700; font-size: 25px; letter-spacing: .3px; }
  .slogan--orange { color: var(--orange); }
  .slogan--blue { color: var(--blue); }

  .brand { font-weight: 700; font-size: 26px; color: var(--blue); display: flex; align-items: center; gap: 6px; }
  .brand__dot { width: 12px; height: 12px; border-radius: 50%; background: var(--orange); display: inline-block; }

  .label { position: absolute; color: var(--label); font-weight: 300; font-size: 62px; letter-spacing: 1px; display: flex; align-items: center; justify-content: center; width: 80px; }
  .label--text { left: 380px; top: 1240px; height: 320px; }
  .label--plain { left: 930px; top: 1200px; height: 400px; }
</style>
</head>
<body>

  <section class="band band--text" aria-label="Bande mit Text">
    <div class="item road road--right road--light" style="top:29px;height:65px" role="img" aria-label="Illustration einer geschwungenen Straße"></div>
    <div class="item road road--left road--teal" style="top:111px;height:114px" role="img" aria-label="Illustration einer geschwungenen Straße"></div>
    <div class="item icon icon--map" style="top:265px;height:40px" role="img" aria-label="Illustration einer Landkarte mit Pin"></div>
    <div class="item icon icon--sign" style="top:330px;height:40px" role="img" aria-label="Illustration eines Wegweisers"></div>
    <div class="item icon icon--compass" style="top:394px;height:22px" role="img" aria-label="Illustration eines Kompasses"></div>
    <div class="item" style="top:497px;height:686px"><span class="vertical slogan slogan--orange">JETZT BUCHEN AUF WWW.WELMORA-HOTELS.DE</span></div>
    <div class="item icon icon--plane" style="top:1213px;height:40px" role="img" aria-label="Illustration eines Flugzeugs"></div>
    <div class="item" style="top:1270px;height:126px"><span class="vertical brand"><span class="brand__dot"></span>welmora</span></div>
    <div class="item icon icon--plane" style="top:1419px;height:40px" role="img" aria-label="Illustration eines Flugzeugs"></div>
    <div class="item" style="top:1494px;height:686px"><span class="vertical slogan slogan--blue">JETZT BUCHEN AUF WWW.WELMORA-HOTELS.DE</span></div>
    <div class="item icon icon--passport" style="top:2253px;height:38px" role="img" aria-label="Illustration eines Reisepasses"></div>
    <div class="item icon icon--camera" style="top:2307px;height:42px" role="img" aria-label="Illustration einer Kamera"></div>
    <div class="item icon icon--suitcase" style="top:2366px;height:28px" role="img" aria-label="Illustration eines Koffers"></div>
    <div class="item road road--left road--light" style="top:2436px;height:65px" role="img" aria-label="Illustration einer geschwungenen Straße"></div>
    <div class="item road road--right road--teal" style="top:2539px;height:128px" role="img" aria-label="Illustration einer geschwungenen Straße"></div>
  </section>

  <div class="label label--text"><span class="vertical">with text</span></div>

  <section class="band band--plain" aria-label="Bande ohne Text">
    <div class="item road road--right road--light" style="top:2px;height:60px" role="img" aria-label="Illustration einer geschwungenen Straße"></div>
    <div class="item road road--left road--green" style="top:67px;height:104px" role="img" aria-label="Illustration einer geschwungenen Straße"></div>
    <div class="item icon icon--map" style="top:178px;height:40px" role="img" aria-label="Illustration einer Landkarte mit Pin"></div>
    <div class="item icon icon--sign" style="top:241px;height:38px" role="img" aria-label="Illustration eines Wegweisers"></div>
    <div class="item icon icon--compass" style="top:307px;height:22px" role="img" aria-label="Illustration eines Kompasses"></div>
    <div class="item" style="top:372px;height:125px"><span class="vertical brand"><span class="brand__dot"></span>welmora</span></div>
    <div class="item icon icon--compass" style="top:552px;height:22px" role="img" aria-label="Illustration eines Kompasses"></div>
    <div class="item icon icon--sign" style="top:606px;height:38px" role="img" aria-label="Illustration eines Wegweisers"></div>
    <div class="item icon icon--map" style="top:671px;height:40px" role="img" aria-label="Illustration einer Landkarte mit Pin"></div>
    <div class="item road road--right road--teal" style="top:797px;height:71px" role="img" aria-label="Illustration einer geschwungenen Straße"></div>
    <div class="item road road--left road--light" style="top:878px;height:77px" role="img" aria-label="Illustration einer geschwungenen Straße"></div>
    <div class="item" style="top:1031px;height:120px"><span class="vertical brand"><span class="brand__dot"></span>welmora</span></div>
    <div class="item icon icon--plane" style="top:1213px;height:40px" role="img" aria-label="Illustration eines Flugzeugs"></div>
    <div class="item" style="top:1273px;height:123px"><span class="vertical brand"><span class="brand__dot"></span>welmora</span></div>
    <div class="item icon icon--plane" style="top:1419px;height:40px" role="img" aria-label="Illustration eines Flugzeugs"></div>
    <div class="item" style="top:1510px;height:120px"><span class="vertical brand"><span class="brand__dot"></span>welmora</span></div>
    <div class="item road road--left road--teal" style="top:1673px;height:98px" role="img" aria-label="Illustration einer geschwungenen Straße"></div>
    <div class="item road road--right road--green" style="top:1804px;height:71px" role="img" aria-label="Illustration einer geschwungenen Straße"></div>
    <div class="item icon icon--suitcase" style="top:1935px;height:27px" role="img" aria-label="Illustration eines Koffers"></div>
    <div class="item icon icon--camera" style="top:1980px;height:44px" role="img" aria-label="Illustration einer Kamera"></div>
    <div class="item icon icon--passport" style="top:2040px;height:40px" role="img" aria-label="Illustration eines Reisepasses"></div>
    <div class="item" style="top:2109px;height:120px"><span class="vertical brand"><span class="brand__dot"></span>welmora</span></div>
    <div class="item icon icon--passport" style="top:2253px;height:38px" role="img" aria-label="Illustration eines Reisepasses"></div>
    <div class="item icon icon--camera" style="top:2307px;height:42px" role="img" aria-label="Illustration einer Kamera"></div>
    <div class="item icon icon--suitcase" style="top:2366px;height:28px" role="img" aria-label="Illustration eines Koffers"></div>
    <div class="item road road--left road--light" style="top:2436px;height:65px" role="img" aria-label="Illustration einer geschwungenen Straße"></div>
    <div class="item road road--right road--teal" style="top:2539px;height:128px" role="img" aria-label="Illustration einer geschwungenen Straße"></div>
  </section>

  <div class="label label--plain"><span class="vertical">without text</span></div>

</body>
</html>
```